KerrLow Farm

Need a nice simple clean double sided business card that has our logo and info on:
Kerr Low Farm
Martin & Felicity Kerr Low
kerrlowfarm@mailbarn.example
Martin: 1-780-555-0148
Felicity: 1-780-555-0193
Instagram @ kerrlow_farm

Contact Information for Business Card

Martin & Felicity Kerr Low kerrlowfarm@mailbarn.example Martin: 1-780-555-0148 Felicity: 1-780-555-0193

```html
<!DOCTYPE html>
<html lang="en">
<head>
<meta charset="utf-8">
<title>Kerr Low Farm — Business Card</title>
<link href="https://fonts.googleapis.com/css2?family=Montserrat:wght@400;500;700&display=swap" rel="stylesheet">
<style>
  :root {
    --page: #e8e8e8;
    --card: #ffffff;
    --green: #4a8c0c;
    --green-deep: #2a5a00;
    --green-bright: #5a9a10;
    --orange: #f39a0e;
    --ink: #333333;
    --white: #ffffff;
  }
  * { margin: 0; padding: 0; box-sizing: border-box; }
  html, body {
    width: 800px; height: 1200px; overflow: hidden;
    background: var(--page);
    font-family: "Montserrat", sans-serif;
  }
  .card {
    position: absolute; left: 90px;
    width: 620px; height: 354px;
    background: var(--card);
    overflow: hidden;
    box-shadow: 0 10px 24px rgba(0,0,0,0.28);
  }
  .card--front { top: 150px; }
  .card--back { top: 660px; }
  .card__art { position: absolute; inset: 0; width: 100%; height: 100%; }

  .wheat {
    position: absolute;
    border-radius: 40%;
    background: radial-gradient(ellipse at center, rgba(243,154,14,0.85) 0%, rgba(243,154,14,0.45) 55%, rgba(243,154,14,0) 75%);
  }
  .wheat--front-top { left: -10px; top: 38px; width: 64px; height: 72px; }
  .wheat--front-bottom { left: 540px; top: 165px; width: 86px; height: 104px; }
  .wheat--back { left: 225px; top: 18px; width: 110px; height: 88px; }

  .brand { position: absolute; text-align: center; }
  .brand__circle {
    display: block; margin: 0 auto;
    border: 3px solid var(--green); border-radius: 50%;
  }
  .brand__name {
    display: block; color: var(--green);
    font-weight: 500; text-transform: uppercase; letter-spacing: 0.04em;
    white-space: nowrap;
  }
  .card--front .brand { left: 0; right: 0; top: 80px; }
  .card--front .brand__circle { width: 98px; height: 98px; }
  .card--front .brand__name { font-size: 25px; margin-top: 12px; }
  .front__email {
    position: absolute; left: 0; right: 0; top: 290px;
    text-align: center; font-size: 14px; letter-spacing: 0.2em; color: var(--ink);
  }

  .card--back .brand { left: 40px; width: 220px; top: 108px; }
  .card--back .brand__circle { width: 78px; height: 78px; }
  .card--back .brand__name { font-size: 19px; margin-top: 10px; }

  .contact { position: absolute; left: 350px; top: 88px; color: var(--white); }
  .contact__title {
    color: var(--orange); font-weight: 700; font-size: 17.5px;
    letter-spacing: 0.04em; text-transform: uppercase; margin-bottom: 12px;
  }
  .contact__person {
    font-weight: 700; font-size: 11px; text-transform: uppercase;
    letter-spacing: 0.03em; margin-top: 6px;
  }
  .contact__line {
    display: flex; align-items: center; gap: 10px;
    font-size: 13.5px; margin-top: 4px;
  }
  .contact__line--gap { margin-top: 10px; }
  .icon {
    width: 18px; height: 18px; border-radius: 50%;
    background: var(--orange); flex: none;
    display: flex; align-items: center; justify-content: center;
  }
  .icon svg { width: 11px; height: 11px; }
</style>
</head>
<body>

<section class="card card--front" aria-label="Card front">
  <svg class="card__art" viewBox="0 0 620 354" aria-hidden="true">
    <defs>
      <linearGradient id="greenFade" x1="0" y1="0" x2="0" y2="1">
        <stop offset="0" stop-color="#5a9a10"/>
        <stop offset="1" stop-color="#2a5a00"/>
      </linearGradient>
    </defs>
    <path d="M0 0 H108 C92 38 62 48 32 54 C16 57 6 64 0 72 Z" fill="url(#greenFade)"/>
    <path d="M450 354 C455 320 490 300 540 290 C585 282 610 268 620 245 V354 Z" fill="url(#greenFade)"/>
  </svg>
  <div class="wheat wheat--front-top" role="img" aria-label="Orange wheat sprigs decoration"></div>
  <div class="wheat wheat--front-bottom" role="img" aria-label="Orange wheat stalks decoration"></div>

  <div class="brand">
    <span class="brand__circle"></span>
    <span class="brand__name">Kerr Low Farm</span>
  </div>
  <p class="front__email">kerrlowfarm@mailbarn.example</p>
</section>

<section class="card card--back" aria-label="Card back">
  <svg class="card__art" viewBox="0 0 620 354" aria-hidden="true">
    <defs>
      <linearGradient id="greenFadeBack" x1="0" y1="0" x2="0" y2="1">
        <stop offset="0" stop-color="#5a9a10"/>
        <stop offset="1" stop-color="#2a5a00"/>
      </linearGradient>
    </defs>
    <path d="M222 0 H620 V354 H319 C290 330 268 300 270 250 C272 190 300 150 290 100 C280 55 255 25 222 0 Z" fill="url(#greenFadeBack)"/>
  </svg>
  <div class="wheat wheat--back" role="img" aria-label="Orange wheat stalks decoration"></div>

  <div class="brand">
    <span class="brand__circle"></span>
    <span class="brand__name">Kerr Low Farm</span>
  </div>

  <div class="contact">
    <p class="contact__title">Kerr Low Farm</p>
    <p class="contact__person">Martin Kerr Low</p>
    <p class="contact__line">
      <span class="icon"><svg viewBox="0 0 24 24"><path fill="#fff" d="M6.6 10.8a15 15 0 0 0 6.6 6.6l2.2-2.2c.3-.3.7-.4 1-.2 1.1.4 2.3.6 3.6.6.6 0 1 .4 1 1V20c0 .6-.4 1-1 1A17 17 0 0 1 3 4c0-.6.4-1 1-1h3.5c.6 0 1 .4 1 1 0 1.3.2 2.5.6 3.6.1.3 0 .7-.2 1z"/></svg></span>
      1-780-555-0148
    </p>
    <p class="contact__person contact__line--gap">Felicity Kerr Low</p>
    <p class="contact__line">
      <span class="icon"><svg viewBox="0 0 24 24"><path fill="#fff" d="M6.6 10.8a15 15 0 0 0 6.6 6.6l2.2-2.2c.3-.3.7-.4 1-.2 1.1.4 2.3.6 3.6.6.6 0 1 .4 1 1V20c0 .6-.4 1-1 1A17 17 0 0 1 3 4c0-.6.4-1 1-1h3.5c.6 0 1 .4 1 1 0 1.3.2 2.5.6 3.6.1.3 0 .7-.2 1z"/></svg></span>
      1-780-555-0193
    </p>
    <p class="contact__line contact__line--gap">
      <span class="icon"><svg viewBox="0 0 24 24"><path fill="#fff" d="M3 5h18v14H3z"/><path fill="none" stroke="#f39a0e" stroke-width="2" d="M3 5l9 8 9-8"/></svg></span>
      kerrlowfarm@mailbarn.example
    </p>
    <p class="contact__line contact__line--gap">
      <span class="icon"></span>
      @ kerrlow_farm
    </p>
  </div>
</section>

</body>
</html>
```